Business Card Design Project

Automotive (vehcle imports & servicing, repairs)business card needed. professional & sleek look needed.

colours same as logo colours pref.

prefer to have few performance logos and Brand names on the card as well.

Target Market(s)

prestige car imports
automotive repairs & service
Automotive compliance workshop

Industry/Entity Type

Automotive

Requirements
Must have
• car brand logos
company details
logo
web address
contact details

```html
<!DOCTYPE html>
<html lang="en">
<head>
<meta charset="UTF-8">
<title>Apex Motorworks – Business Card</title>
<link rel="stylesheet" href="https://fonts.googleapis.com/css2?family=Exo+2:wght@400;600;700&display=swap">
<style>
  :root {
    --backdrop: #b9b9bb;
    --brand-red: #d71920;
    --ink: #1b1b1b;
    --paper: #ffffff;
    --muted: #555555;
    --faint: #efefef;
    --card-w: 560px;
    --card-h: 320px;
  }
  * { box-sizing: border-box; margin: 0; padding: 0; }
  html, body { width: 1200px; height: 900px; overflow: hidden; }
  body {
    background: var(--backdrop);
    font-family: "Exo 2", sans-serif;
    position: relative;
  }
  .card {
    position: absolute;
    width: var(--card-w);
    height: var(--card-h);
    overflow: hidden;
    box-shadow: 0 10px 28px rgba(0,0,0,.22);
  }

  /* Name lockup: one plain circle + company name in one colour and weight */
  .brand-lockup {
    position: absolute;
    display: flex;
    align-items: center;
    gap: 14px;
    white-space: nowrap;
  }
  .brand-mark {
    border-radius: 50%;
    background: var(--ink);
    flex: none;
  }
  .brand-name {
    font-weight: 700;
    text-transform: uppercase;
    letter-spacing: .5px;
    line-height: 1;
  }
  .web-address {
    position: absolute;
    font-weight: 600;
    letter-spacing: 2px;
    white-space: nowrap;
  }

  /* Front */
  .card-front { left: 80px; top: 100px; background: var(--brand-red); }
  .card-front .brand-lockup { left: 70px; top: 128px; }
  .card-front .brand-mark { width: 56px; height: 56px; }
  .card-front .brand-name { color: var(--paper); font-size: 34px; }
  .card-front .web-address { left: 140px; top: 198px; color: var(--paper); font-size: 17px; }

  /* Back */
  .card-back { left: 560px; top: 480px; background: var(--paper); }
  .card-back .brand-lockup { left: 40px; top: 44px; }
  .card-back .brand-mark { width: 44px; height: 44px; }
  .card-back .brand-name { color: var(--ink); font-size: 24px; }
  .card-back .web-address { left: 98px; top: 94px; color: var(--brand-red); font-size: 14px; }

  .backdrop-disc {
    position: absolute;
    right: 40px; top: 100px;
    width: 160px; height: 160px;
    border-radius: 50%;
    background: var(--faint);
  }
  .holder {
    position: absolute;
    right: 34px; top: 40px;
    text-align: right;
  }
  .holder-name { color: var(--brand-red); font-weight: 600; font-size: 21px; }
  .holder-role { color: var(--muted); font-size: 12px; }

  .contact {
    position: absolute;
    left: 60px; bottom: 52px;
    width: 250px;
    text-align: right;
    font-style: normal;
    font-size: 12.5px;
    line-height: 1.35;
    color: var(--ink);
  }
  .contact-address { font-weight: 600; font-size: 14px; margin-bottom: 2px; }
  .contact-label { color: var(--brand-red); }

  .footer-rule {
    position: absolute;
    left: 0; right: 0; bottom: 26px;
    height: 2px;
    background: var(--ink);
  }
  .footer-band {
    position: absolute;
    left: 0; right: 0; bottom: 0;
    height: 22px;
    background: var(--brand-red);
  }
</style>
</head>
<body>

  <section class="card card-front" aria-label="Business card front">
    <div class="brand-lockup">
      <span class="brand-mark"></span>
      <span class="brand-name">Apex Motorworks</span>
    </div>
    <p class="web-address">apexmw.com.au</p>
  </section>

  <section class="card card-back" aria-label="Business card back">
    <div class="backdrop-disc"></div>
    <div class="brand-lockup">
      <span class="brand-mark"></span>
      <span class="brand-name">Apex Motorworks</span>
    </div>
    <p class="web-address">apexmw.com.au</p>

    <div class="holder">
      <p class="holder-name">Daniel Marsh</p>
      <p class="holder-role">Director</p>
    </div>

    <address class="contact">
      <p class="contact-address">12 Kingsley Rd, Eastfield,<br>Victoria 3199, Australia</p>
      <p><span class="contact-label">Phone:</span> +61 3 9000 1234</p>
      <p><span class="contact-label">Fax:</span> +61 3 9000 1235</p>
      <p><span class="contact-label">Mobile:</span> +61 400 000 123</p>
      <p><span class="contact-label">Email:</span> daniel@apexmw.com.au</p>
    </address>

    <div class="footer-rule"></div>
    <div class="footer-band"></div>
  </section>

</body>
</html>
```